Community Youth Organisation needs a flyer template design for youth workshop

We require a flyer design that can be used for ongoing youth workshops targetted at young people 11-19 with intellectual disabilities (including Autism and Aspergers). We are hoping the flyer can be used over and over again when advertising our upcoming youth workshop series. Each workshop series will be approx 5 weeks and will be based on a particular topic. For example, our first workshop series will be run every Monday afternoon for 5 weeks on the topic "Conflict and Anger Management" (see attached info). We will then run a different workshop series on a different topic so we would like the same design to be used however with the possibility of editing the specific workshop info on it (e.g. dates, topic). We would require our BRTW logo on the flyer and graphics that would grab the attention of young people aged 11-19 with intellectual disabilities.

Target Market(s)

young people aged 11-19 with intellectual disabilities and their parents/carers

Industry/Entity Type

Advertising

Requirements
Must have
• BRTW Logo as prominent
Information as provided in attachment however in any "look" you feel would be appealing to the target group

```html
<!DOCTYPE html>
<html lang="en">
<head>
<meta charset="utf-8">
<title>Youth Workshops Flyer</title>
<link href="https://fonts.googleapis.com/css2?family=Fredoka:wght@500;600&family=Open+Sans:wght@400;600;700;800&display=swap" rel="stylesheet">
<style>
  :root {
    --sky-top: #8fd0f0;
    --sky-pale: #e3f4fc;
    --panel: #f4fbff;
    --blue: #1b6db3;
    --blue-dark: #134f86;
    --red: #d6262e;
    --yellow: #ffd23f;
    --orange: #f7941d;
    --green: #7cc242;
    --green-dark: #4f9a2a;
    --text: #1e2a38;
    --white: #ffffff;
  }
  * { box-sizing: border-box; margin: 0; padding: 0; }
  html, body { width: 849px; height: 1200px; overflow: hidden; background: #ffffff; }
  body { font-family: "Open Sans", Arial, sans-serif; color: var(--text); }

  .flyer {
    position: relative;
    width: 849px; height: 1200px;
    background: linear-gradient(180deg, var(--sky-top) 0%, var(--sky-pale) 22%, var(--panel) 45%, var(--sky-pale) 62%, var(--sky-top) 100%);
    overflow: hidden;
  }

  .header {
    height: 140px;
    display: flex; align-items: center; justify-content: center;
  }
  .title {
    font-family: "Fredoka", "Comic Sans MS", sans-serif; font-weight: 600;
    font-size: 78px; line-height: 1; letter-spacing: 1px;
    white-space: nowrap;
    text-shadow: 0 4px 0 rgba(19,79,134,.25);
  }
  .title .youth { color: var(--blue); }
  .title .workshops { color: var(--orange); }

  .intro { padding: 6px 60px 0 60px; font-size: 15.5px; line-height: 1.5; }
  .intro p + p { margin-top: 12px; }
  .intro strong { color: var(--blue-dark); }

  .workshop-title {
    margin: 26px 60px 0 60px;
    font-size: 24px; font-weight: 800; color: var(--blue-dark);
    text-transform: uppercase; letter-spacing: .5px;
  }
  .workshop-title .topic { color: var(--red); }
  .workshop-rule { margin: 8px 60px 0 60px; height: 3px; background: var(--red); }

  .workshop-desc { margin: 12px 60px 0 60px; font-size: 15px; line-height: 1.5; }

  .schedule {
    margin: 20px 60px 0 60px; width: 729px;
    border-collapse: collapse; background: var(--white);
    font-size: 15px;
  }
  .schedule th {
    background: var(--blue); color: var(--white);
    font-weight: 700; text-transform: uppercase; letter-spacing: 1px;
    padding: 9px 12px; text-align: center; border: 2px solid var(--blue-dark);
  }
  .schedule td { border: 2px solid #a9cde8; padding: 7px 14px; }
  .schedule .date { width: 255px; }
  .schedule .time, .schedule .location { text-align: center; vertical-align: middle; line-height: 1.5; }
  .schedule .location strong { display: block; color: var(--blue-dark); }
  .brand-inline {
    display: inline-flex; align-items: center; gap: 6px; margin-top: 6px;
    font-weight: 800; color: var(--blue); font-size: 18px;
  }
  .brand-dot { width: 14px; height: 14px; border-radius: 50%; background: var(--blue); }

  .register { margin: 26px 60px 0 60px; text-align: center; }
  .register h2 { font-size: 24px; font-weight: 800; color: var(--blue-dark); text-transform: uppercase; }
  .register .contact { margin-top: 6px; font-size: 16px; }
  .register .contact b { color: var(--red); font-size: 24px; font-weight: 800; }
  .register .note { margin-top: 10px; font-size: 13px; line-height: 1.45; color: #35465a; }

  .scene-art {
    position: absolute; left: 0; right: 0; bottom: 0; height: 320px;
    background: linear-gradient(180deg, rgba(143,208,240,0) 0%, #a6d96a 45%, var(--green) 70%, var(--green-dark) 100%);
  }
  .footer-brand {
    position: absolute; right: 40px; bottom: 28px;
    display: flex; align-items: center; gap: 10px;
    background: var(--white); padding: 10px 18px; border-radius: 8px;
    font-weight: 800; font-size: 28px; color: var(--blue);
  }
  .footer-brand .brand-dot { width: 22px; height: 22px; }
</style>
</head>
<body>
<main class="flyer">
  <header class="header">
    <h1 class="title"><span class="youth">Youth</span> <span class="workshops">Workshops</span></h1>
  </header>

  <section class="intro">
    <p>The <strong>BRTW Brookvale Regional Teen Welfare Workshop Series</strong> caters for young people between the ages of 11 - 19 years with intellectual disabilities as well as those with Autism Spectrum Disorder, Asperger's and ADHD.</p>
    <p>Workshops provide young people with an opportunity to socialise with their peers while learning essential life skills. They include a combination of hands on activities, group work and discussion. All workshops include afternoon tea and are provided free of charge.</p>
  </section>

  <h2 class="workshop-title">Workshop 1: <span class="topic">Conflict and Anger Management</span></h2>
  <div class="workshop-rule"></div>
  <p class="workshop-desc">During the workshops participants will learn to identify the physical and emotional symptoms of anger, understand what their personal triggers are, learn techniques to express their emotions in a positive manner and discover appropriate ways to respond to bullying behaviours.</p>

  <table class="schedule">
    <thead>
      <tr><th>Date</th><th>Time</th><th>Location</th></tr>
    </thead>
    <tbody>
      <tr>
        <td class="date">Monday 15 April 2013</td>
        <td class="time" rowspan="5">Every workshop is<br>3:15pm - 5:00pm</td>
        <td class="location" rowspan="5"><strong>BRTW</strong>24 Larch Street<br>Brookvale QLD 4300<br><span class="brand-inline"><span class="brand-dot"></span>BRTW</span></td>
      </tr>
      <tr><td class="date">Monday 22 April 2013</td></tr>
      <tr><td class="date">Monday 29 April 2013</td></tr>
      <tr><td class="date">Monday 6 May 2013</td></tr>
      <tr><td class="date">Monday 13 May 2013</td></tr>
    </tbody>
  </table>

  <section class="register">
    <h2>How to register:</h2>
    <p class="contact">To register simply contact Dana Morgan, Youth and Family Worker<br>via phone <b>3900 2471</b> or email <b>hello@brtw.org.au</b></p>
    <p class="note">Please be aware that participants are served on a first come first served basis and that by registering for a workshop series participants are agreeing to attend all sessions.</p>
  </section>

  <div class="scene-art" role="img" aria-label="Cartoon park scene with trees, grass and a group of young people playing"></div>
  <div class="footer-brand"><span class="brand-dot"></span>BRTW</div>
</main>
</body>
</html>
```